Builders Worksite Corflute Outdoor Sign

We are a building company who are just branching out into new construction. How first new build is our own home which was designed by us and a local architect. We are proud and want to create more advertisement around our business.

We need a corflute sign that can staked outside the construction site and can be seen by people passing by.
Updates

Can we please make the company name and logo bigger (Tidewater Ridge Homes) This needs to be the focus. Can we please replace 'Manu' with 'Contact Us on 021-574-3619'

Target Market(s)

Home owners and people wishing to build on lifestyle blocks in New Zealand.

Font styles to use
Sans Serif

Requirements
Must have
• It needs to feature our:
Logo
Company name
Contact name and number - Manu - 0215743619
Landscape NOT portrait.

```html
<!DOCTYPE html>
<html lang="en">
<head>
<meta charset="utf-8">
<title>Tidewater Ridge Homes – Site Sign Concepts</title>
<link href="https://fonts.googleapis.com/css2?family=Montserrat:wght@500;700;800&display=swap" rel="stylesheet">
<style>
  :root{
    --navy:#19202e;
    --gold:#e6b220;
    --gold-deep:#d39a2c;
    --white:#ffffff;
    --paper:#f4f4f4;
  }
  html,body{margin:0;padding:0;overflow:hidden}
  body{width:1200px;height:2495px;background:var(--white);position:relative;font-family:"Montserrat",Arial,sans-serif}
  .sign{position:absolute;left:242px;width:716px;height:537px;overflow:hidden;background:var(--white);
        box-shadow:2px 2px 2px rgba(0,0,0,.35)}
  .sign--one{top:82px;background:linear-gradient(180deg,#fafafa 0%,#ececec 60%,#e2e2e2 100%)}
  .sign--two{top:683px}
  .sign--three{top:1281px}
  .sign--four{top:1878px;background:var(--navy)}
  .layer{position:absolute;left:0;top:0;width:716px;height:537px}
  .line{position:absolute;left:0;width:100%;text-align:center;white-space:nowrap;margin:0}
  .brand{position:absolute;left:0;width:100%;display:flex;flex-direction:column;align-items:center}
  .brand__dot{width:50px;height:50px;border-radius:50%;background:var(--gold);margin-bottom:14px}
  .brand__name{font-weight:500;font-size:23px;letter-spacing:2px;color:var(--navy);text-align:center;line-height:1.25}
  .sign--four .brand__name{color:var(--white)}
  .headline{font-weight:800;font-size:54px;line-height:1;letter-spacing:1px}
  .headline--big{font-size:64px}
  .headline--xl{font-size:84px}
  .contact-label{font-weight:700;font-size:27px;letter-spacing:1.5px}
  .phone{font-weight:800;font-size:54px;letter-spacing:1px;display:flex;justify-content:center;align-items:center;gap:14px}
  .phone svg{width:46px;height:46px}
  .pill{display:inline-block;border-radius:14px;padding:2px 20px}
  .band{position:absolute;left:0;width:100%}
  .c-navy{color:var(--navy)} .c-gold{color:var(--gold)} .c-white{color:var(--white)}
</style>
</head>
<body>
<svg width="0" height="0" style="position:absolute" aria-hidden="true">
  <symbol id="icon-phone" viewBox="0 0 24 24"><path fill="currentColor" d="M6.6 10.8c1.4 2.8 3.8 5.1 6.6 6.6l2.2-2.2c.3-.3.7-.4 1-.2 1.1.4 2.3.6 3.6.6.6 0 1 .4 1 1V20c0 .6-.4 1-1 1C10.6 21 3 13.4 3 4c0-.6.4-1 1-1h3.5c.6 0 1 .4 1 1 0 1.3.2 2.5.6 3.6.1.3 0 .7-.2 1z"/></symbol>
</svg>

<!-- Concept 1: roof base -->
<section class="sign sign--one">
  <div class="brand" style="top:36px">
    <div class="brand__dot"></div>
    <div class="brand__name">TIDEWATER RIDGE<br>HOMES</div>
  </div>
  <p class="line headline c-gold" style="top:198px">TIDEWATER RIDGE</p>
  <p class="line headline headline--big c-navy" style="top:262px">HOMES</p>
  <svg class="layer" viewBox="0 0 716 537" aria-hidden="true">
    <polygon points="0,496 347,356 716,502 716,514 347,370 0,510" fill="var(--gold)"/>
    <polygon points="0,512 347,372 716,516 716,537 0,537" fill="var(--navy)"/>
  </svg>
  <p class="line contact-label c-white" style="top:430px">CONTACT US ON</p>
  <p class="line phone c-white" style="top:468px"><svg class="c-gold"><use href="#icon-phone"/></svg>021-574-3619</p>
</section>

<!-- Concept 2: navy and gold bands -->
<section class="sign sign--two">
  <div class="brand" style="top:30px">
    <div class="brand__dot"></div>
    <div class="brand__name">TIDEWATER RIDGE<br>HOMES</div>
  </div>
  <div class="band" style="top:196px;height:8px;background:var(--gold)"></div>
  <div class="band" style="top:204px;height:178px;background:var(--navy)"></div>
  <div class="band" style="top:388px;height:149px;background:var(--gold)"></div>
  <p class="line headline c-white" style="top:228px">TIDEWATER RIDGE</p>
  <p class="line headline headline--big c-gold" style="top:300px">HOMES</p>
  <p class="line contact-label c-navy" style="top:404px"><span class="pill" style="background:var(--white)">CONTACT US ON</span></p>
  <p class="line phone c-navy" style="top:450px"><svg class="c-white"><use href="#icon-phone"/></svg>021-574-3619</p>
</section>

<!-- Concept 3: gold gradient headline block -->
<section class="sign sign--three">
  <div class="brand" style="top:30px">
    <div class="brand__dot"></div>
    <div class="brand__name">TIDEWATER RIDGE<br>HOMES</div>
  </div>
  <div class="band" style="top:200px;height:226px;background:linear-gradient(180deg,var(--gold) 0%,var(--gold-deep) 100%)"></div>
  <p class="line headline headline--big c-navy" style="top:216px;font-size:62px">TIDEWATER RIDGE</p>
  <p class="line headline headline--xl c-white" style="top:292px">HOMES</p>
  <p class="line contact-label c-white" style="top:400px"><span class="pill" style="background:var(--navy);padding:4px 28px">CONTACT US ON</span></p>
  <p class="line phone c-navy" style="top:452px"><svg class="c-gold"><use href="#icon-phone"/></svg>021-574-3619</p>
</section>

<!-- Concept 4: navy roof header -->
<section class="sign sign--four">
  <div class="brand" style="top:32px">
    <div class="brand__dot" style="background:var(--white)"></div>
    <div class="brand__name">TIDEWATER RIDGE<br>HOMES</div>
  </div>
  <svg class="layer" viewBox="0 0 716 537" aria-hidden="true">
    <polygon points="0,298 358,212 716,296 716,537 0,537" fill="var(--gold)"/>
    <polygon points="0,304 358,226 716,300 716,537 0,537" fill="var(--white)"/>
  </svg>
  <p class="line headline c-navy" style="top:280px;font-size:50px">TIDEWATER RIDGE</p>
  <p class="line headline c-gold" style="top:338px;font-size:58px">HOMES</p>
  <p class="line contact-label c-navy" style="top:414px;font-size:24px">CONTACT US ON</p>
  <div style="position:absolute;left:60px;width:595px;top:446px;height:62px;border-radius:14px;background:linear-gradient(180deg,var(--gold),var(--gold-deep));box-shadow:0 6px 6px rgba(0,0,0,.25)"></div>
  <p class="line phone c-navy" style="top:446px;line-height:62px"><svg class="c-white"><use href="#icon-phone"/></svg>021-574-3619</p>
</section>
</body>
</html>
```